Webdesign
Zielgruppe
Briefing für die neue Website von KOLVENO GmbH
Allgemeine Informationen:
Name des Unternehmens: KOLVENO GmbH
Branche: Maschinenbau
Zweck der Website: Eine Unternehmenswebsite, die informiert, was die Firma macht und es potenziellen Kunden oder Partnern ermöglicht, in Kontakt zu treten.
Zielgruppe:
Hauptzielgruppe: Anlagenbauer, Maschinenbauer, Anlagenbetreiber aus verschiedenen Branchen.
Design-Anforderungen: Die Zielgruppe erwartet Professionalität und Klarheit, also sollte die Website eine hohe Qualität, Professionalität und Benutzerfreundlichkeit reflektieren.
Design-Vorlieben:
Farbschema & Stil: Das Design sollte sich an den bereitgestellten Logos orientieren. Der gewünschte Stil ist modern und klar.
Inspirationsquellen: Die Logos des Unternehmens, die dem Briefing beigefügt werden.
Inhalt und Struktur:
Einseitiges Design: Die Website sollte nur eine Seite zum Herunterscrollen haben.
Unternehmensvorstellung: Ein kurzer Abschnitt, der beschreibt, wer KOLVENO GmbH ist und was das Unternehmen macht.
Leistungsübersicht: Eine klare Darstellung der Dienstleistungen oder Produkte, die KOLVENO GmbH anbietet. Dies kann durch Symbole, kurze Texte oder Bilder dargestellt werden.
Kontaktmöglichkeit: Ein Kontaktformular oder zumindest klare Kontaktinformationen (Telefon, E-Mail, Adresse), so dass Besucher leicht in Kontakt treten können.
Aufgabenstellung
siehe oben

```html
<!DOCTYPE html>
<html lang="de">
<head>
<meta charset="utf-8">
<title>KOLVENO GmbH – Maschinenbau</title>
<link rel="stylesheet" href="https://fonts.googleapis.com/css2?family=Montserrat:wght@400;500;600;700&display=swap">
<style>
:root{
  --red:#b30b0b;
  --black:#0b0b0b;
  --footer:#232323;
  --grey-card:#e6e6e6;
  --grey-section:#ebebeb;
  --ring-dark:#2f2f2f;
  --text:#3a3a3a;
  --white:#ffffff;
}
*{margin:0;padding:0;box-sizing:border-box}
html,body{width:1200px;height:3315px;overflow:hidden}
body{font-family:'Montserrat',sans-serif;color:var(--text);background:var(--white);position:relative}
.abs{position:absolute}

.topbar{left:0;top:0;width:1200px;height:38px;background:var(--black);color:#ddd;font-size:12px}
.topbar .mail{left:151px;top:12px;display:flex;align-items:center;gap:9px}
.topbar .phone{right:152px;top:10px;display:flex;align-items:center;gap:9px;font-size:15px;letter-spacing:.5px}

.nav{left:0;top:38px;width:1200px;height:73px;background:var(--white)}
.logo{display:flex;align-items:center;gap:8px;font-weight:700;font-size:20px;letter-spacing:.5px}
.nav .logo{left:150px;top:24px;color:var(--red)}
.logo .dot{width:18px;height:18px;border-radius:50%;background:currentColor}
.menu{left:659px;top:0;height:73px;display:flex;font-size:13px;font-weight:500;color:#222}
.menu a{display:flex;align-items:center;height:73px;padding:0 14px;color:inherit;text-decoration:none}
.menu a.active{background:var(--red);color:var(--white);font-weight:600;width:90px;justify-content:center;padding:0}
.menu a:nth-child(2){margin-left:8px}
.menu a:nth-child(3),.menu a:nth-child(4){margin-left:10px}

.hero{left:0;top:111px;width:1200px;height:449px;overflow:hidden;
  background:
    radial-gradient(ellipse 170px 300px at 690px 300px,rgba(22,28,46,.95) 0%,rgba(22,28,46,.7) 60%,rgba(22,28,46,0) 100%),
    radial-gradient(ellipse 420px 260px at 600px 40px,rgba(200,130,60,.55) 0%,rgba(200,130,60,0) 100%),
    linear-gradient(180deg,#4a3523 0%,#3a2618 45%,#2a1a10 75%,#1a100a 100%)}
.hero::after{content:"";position:absolute;inset:0;background:linear-gradient(90deg,rgba(0,0,0,.35) 0%,rgba(0,0,0,0) 45%,rgba(0,0,0,.15) 100%)}
.hero h1,.hero .lead,.hero .btn-call,.hero .hero-dots{z-index:1}
.hero h1{left:147px;top:133px;width:480px;color:var(--white);font-size:37px;line-height:44px;font-weight:600}
.hero .lead{left:149px;top:232px;color:var(--white);font-size:16px}
.btn-call{left:151px;top:285px;width:228px;height:48px;background:var(--red);color:var(--white);font-size:18px;font-weight:700;display:flex;align-items:center;justify-content:center;gap:12px}
.hero-dots{left:566px;top:417px;display:flex;gap:7px}
.hero-dots i{width:8px;height:8px;border-radius:50%;background:var(--red)}
.hero-dots i:first-child{background:var(--white)}

.section-title{color:var(--red);font-size:26px;font-weight:600}
.about-title{left:148px;top:720px}
.about-text{left:148px;top:764px;width:525px;font-size:16px;line-height:25px;color:#555}
.about-visual{left:730px;top:614px;width:326px;height:358px}

.services-title{left:0;top:1045px;width:1200px;text-align:center}
.card{width:417px;height:366px;background:var(--grey-card)}
.card .photo{left:0;top:0;width:417px;height:223px}
.card .photo.a{background:linear-gradient(160deg,#3b3f44 0%,#8c949c 35%,#5a7ea8 70%,#2f5e96 100%)}
.card .photo.b{background:linear-gradient(160deg,#dfe3e8 0%,#a7b0ba 45%,#8e7563 75%,#c7cdd3 100%)}
.card .photo.c{background:linear-gradient(160deg,#1d3148 0%,#3c5570 40%,#9a7d3a 75%,#c79a2e 100%)}
.card .photo.d{background:linear-gradient(160deg,#eceef0 0%,#aab1b8 45%,#6e757c 75%,#c3c8cd 100%)}
.card .label{left:0;top:185px;width:417px;height:38px;background:rgba(179,11,11,.92);color:var(--white);font-size:19px;font-weight:600;padding:8px 0 0 17px}
.card p{left:24px;top:250px;width:375px;font-size:12.4px;line-height:19px;color:#333}

.strengths{left:0;top:1958px;width:1200px;height:406px;background:var(--red)}
.strengths h2{left:0;top:28px;width:1200px;text-align:center;color:var(--white);font-size:26px;font-weight:600}
.strength{top:89px;color:var(--white)}
.strength svg{display:block;height:60px}
.strength h3{margin-top:26px;font-size:15.5px;font-weight:600;line-height:18px}
.strength p{margin-top:8px;font-size:12px;line-height:16.4px;color:#f1d0d0}
.divider{top:92px;width:1px;height:276px;background:rgba(255,255,255,.35)}

.quote-mark{color:#dcdcdc;font-size:96px;font-weight:700;line-height:1;font-family:Georgia,serif}
.testi-title{left:0;top:2428px;width:1200px;text-align:center}
.testi{top:2500px;width:405px;font-size:12.7px;line-height:19px;color:#444}
.testi .name{margin-top:16px;color:var(--red);font-weight:600;font-size:12.5px}
.testi-dots{left:566px;top:2682px;display:flex;gap:7px}
.testi-dots i{width:6px;height:6px;border-radius:50%;background:#c8c8c8}
.testi-dots i:first-child{background:var(--red)}

.contact{left:0;top:2755px;width:1200px;height:358px;background:var(--grey-section)}
.contact h2{left:225px;top:38px}
.contact .sub{left:228px;top:79px;font-size:12.5px;color:#333}
.field{background:var(--white);font-size:12.5px;color:#444;padding:10px 13px}
.btn-send{left:413px;top:289px;width:169px;height:37px;background:var(--red);color:var(--white);font-weight:700;font-size:15px;display:flex;align-items:center;justify-content:center;letter-spacing:.5px}
.contact-visual{left:805px;top:40px;width:380px;height:300px;border-radius:6px;
  background:linear-gradient(115deg,rgba(235,235,235,0) 0%,rgba(214,32,32,.55) 25%,rgba(150,30,40,.6) 45%,rgba(180,175,210,.55) 70%,rgba(235,235,235,0) 100%)}

.info{left:0;top:3113px;width:1200px;height:121px;background:var(--white)}
.info .item{display:flex;align-items:flex-start;gap:16px;color:#444}
.info .addr{left:233px;top:25px;font-size:13px;line-height:19px}
.info .mail{left:542px;top:26px;font-size:16px}
.info .tel{left:798px;top:24px;font-size:19px}

.footer{left:0;top:3234px;width:1200px;height:81px;background:var(--footer);color:var(--white)}
.footer .logo{left:151px;top:29px;color:var(--white)}
.social{left:536px;top:35px;display:flex;gap:21px}
.social i{width:10px;height:10px;border-radius:50%;background:var(--white)}
.copy{left:945px;top:32px;font-size:13px}
</style>
</head>
<body>

<header class="abs topbar">
  <div class="abs mail">
    <svg width="16" height="12" viewBox="0 0 16 12" fill="none" stroke="#ddd" stroke-width="1.3"><rect x="1" y="1" width="14" height="10"/><path d="M1 1l7 6 7-6"/></svg>
    kontakt@kolveno.de
  </div>
  <div class="abs phone">
    <svg width="15" height="15" viewBox="0 0 24 24" fill="none" stroke="#ddd" stroke-width="2"><path d="M22 16.9v3a2 2 0 0 1-2.2 2 19.8 19.8 0 0 1-8.6-3.1 19.5 19.5 0 0 1-6-6A19.8 19.8 0 0 1 2.1 4.2 2 2 0 0 1 4.1 2h3a2 2 0 0 1 2 1.7c.1.9.4 1.8.7 2.7a2 2 0 0 1-.5 2.1L8 9.8a16 16 0 0 0 6 6l1.3-1.3a2 2 0 0 1 2.1-.4c.9.3 1.8.6 2.7.7a2 2 0 0 1 1.7 2z"/></svg>
    0800.472.915
  </div>
</header>

<nav class="abs nav">
  <div class="abs logo"><span class="dot"></span>KOLVENO GmbH</div>
  <div class="abs menu">
    <a class="active" href="#">Startseite</a>
    <a href="#">Wer wir sind</a>
    <a href="#">Was wir tun</a>
    <a href="#">Kontakt</a>
  </div>
</nav>

<section class="abs hero" role="img" aria-label="Ingenieur mit Schutzhelm in einer beleuchteten Fertigungshalle, von hinten gesehen">
  <h1 class="abs">Lorem ipsum dolor sit amet, consectetur</h1>
  <p class="abs lead">Lorem ipsum dolor sit amet, consectetur</p>
  <div class="abs btn-call">
    <svg width="18" height="18" viewBox="0 0 24 24" fill="none" stroke="#fff" stroke-width="2"><path d="M22 16.9v3a2 2 0 0 1-2.2 2 19.8 19.8 0 0 1-8.6-3.1 19.5 19.5 0 0 1-6-6A19.8 19.8 0 0 1 2.1 4.2 2 2 0 0 1 4.1 2h3a2 2 0 0 1 2 1.7c.1.9.4 1.8.7 2.7a2 2 0 0 1-.5 2.1L8 9.8a16 16 0 0 0 6 6l1.3-1.3a2 2 0 0 1 2.1-.4c.9.3 1.8.6 2.7.7a2 2 0 0 1 1.7 2z"/></svg>
    0800.472.915
  </div>
  <div class="abs hero-dots"><i></i><i></i><i></i><i></i><i></i></div>
</section>

<h2 class="abs section-title about-title">Wer wir sind</h2>
<p class="abs about-text">KOLVENO ist ein führendes Unternehmen im Bereich moderner Maschinenbau. Wir sind spezialisiert auf die Konzeption, Konstruktion und Herstellung maßgeschneiderter Maschinen und Anlagen, die den höchsten Ansprüchen der heutigen Industrie gerecht werden.</p>
<svg class="abs about-visual" viewBox="0 0 326 358" role="img" aria-label="Runde Aufnahme einer hellen Produktionsanlage in einem rot-dunkelgrauen Rahmen">
  <defs>
    <radialGradient id="plant" cx="50%" cy="45%" r="60%">
      <stop offset="0" stop-color="#e3e6ea"/>
      <stop offset=".55" stop-color="#9aa1a8"/>
      <stop offset="1" stop-color="#4b5056"/>
    </radialGradient>
  </defs>
  <path d="M28 179 A135 135 0 0 1 298 179" fill="none" stroke="var(--ring-dark)" stroke-width="26"/>
  <path d="M298 179 A135 135 0 0 1 28 179" fill="none" stroke="var(--red)" stroke-width="26"/>
  <circle cx="163" cy="179" r="114" fill="#ffffff"/>
  <circle cx="163" cy="179" r="108" fill="url(#plant)"/>
</svg>

<h2 class="abs section-title services-title">Was wir tun</h2>

<article class="abs card" style="left:151px;top:1110px">
  <div class="abs photo a" role="img" aria-label="Pneumatische Fertigungsanlage mit blauen Schläuchen"></div>
  <div class="abs label">Quis ipsum suspendisse</div>
  <p class="abs">Lorem ipsum dolor sit amet, consectetur adipiscing elit, sed do eiusmod tempor incididunt ut labore et dolore magna aliqua. Quis ipsum suspendisse ultrices gravida.&nbsp; Sed do eiusmod tempor incididunt ut labore et dolore magna aliqua. Quis ipsum suspendisse ultrices gravida.</p>
</article>
<article class="abs card" style="left:633px;top:1110px">
  <div class="abs photo b" role="img" aria-label="Helle Fabrikhalle mit Roboterzellen"></div>
  <div class="abs label">Quis ipsum suspendisse</div>
  <p class="abs">Lorem ipsum dolor sit amet, consectetur adipiscing elit, sed do eiusmod tempor incididunt ut labore et dolore magna aliqua. Quis ipsum suspendisse ultrices gravida.&nbsp; Sed do eiusmod tempor incididunt ut labore et dolore magna aliqua. Quis ipsum suspendisse ultrices gravida.</p>
</article>
<article class="abs card" style="left:151px;top:1523px">
  <div class="abs photo c" role="img" aria-label="Gelbe Industrieroboterarme mit digitalen Symbolen"></div>
  <div class="abs label">Quis ipsum suspendisse</div>
  <p class="abs">Lorem ipsum dolor sit amet, consectetur adipiscing elit, sed do eiusmod tempor incididunt ut labore et dolore magna aliqua. Quis ipsum suspendisse ultrices gravida.&nbsp; Sed do eiusmod tempor incididunt ut labore et dolore magna aliqua. Quis ipsum suspendisse ultrices gravida.</p>
</article>
<article class="abs card" style="left:633px;top:1523px">
  <div class="abs photo d" role="img" aria-label="Automatisierte Abfüllanlage in heller Halle"></div>
  <div class="abs label">Quis ipsum suspendisse</div>
  <p class="abs">Lorem ipsum dolor sit amet, consectetur adipiscing elit, sed do eiusmod tempor incididunt ut labore et dolore magna aliqua. Quis ipsum suspendisse ultrices gravida.&nbsp; Sed do eiusmod tempor incididunt ut labore et dolore magna aliqua. Quis ipsum suspendisse ultrices gravida.</p>
</article>

<section class="abs strengths">
  <h2 class="abs">Unsere Stärken</h2>

  <div class="abs strength" style="left:153px;width:150px">
    <svg width="48" viewBox="0 0 48 60" fill="none" stroke="#fff" stroke-width="1.8"><circle cx="24" cy="24" r="15"/><circle cx="24" cy="24" r="5"/><path d="M18 40v8h12v-8M19 52h10M24 2v5M5 24H1M47 24h-4M9 9l3 3M39 9l-3 3"/></svg>
    <h3>INNOVATION</h3>
    <p>Wir setzen modernste CAD/CAM-Software und CNC-Technologien ein, um Präzision und Effizienz in der Produktion sicherzustellen.</p>
  </div>
  <div class="abs divider" style="left:315px"></div>

  <div class="abs strength" style="left:343px;width:148px">
    <svg width="48" viewBox="0 0 48 60" fill="none" stroke="#fff" stroke-width="1.8"><circle cx="24" cy="22" r="19"/><circle cx="24" cy="22" r="12"/><path d="M24 15l2 5h5l-4 3 2 5-5-3-5 3 2-5-4-3h5z"/><path d="M14 38l-4 18 8-5 4 7M34 38l4 18-8-5-4 7"/></svg>
    <h3>QUALITÄT</h3>
    <p>Unsere hochqualifizierten Ingenieure und Techniker arbeiten mit Leidenschaft daran, innovative Lösungen zu entwickeln und höchste Qualitätsstandards zu erfüllen.</p>
  </div>
  <div class="abs divider" style="left:503px"></div>

  <div class="abs strength" style="left:531px;width:150px">
    <svg width="56" viewBox="0 0 56 60" fill="none" stroke="#fff" stroke-width="1.8"><path d="M46 14A24 24 0 1 0 52 32"/><path d="M46 4v10h-10"/><path d="M30 12L20 32h9l-4 16 12-22h-9z"/></svg>
    <h3>NACHHALTIGKEIT</h3>
    <p>Umweltfreundlichkeit und Nachhaltigkeit sind integraler Bestandteil unserer Philosophie. Wir integrieren diese Prinzipien in all unsere Produkte und Produktionsprozesse.</p>
  </div>
  <div class="abs divider" style="left:699px"></div>

  <div class="abs strength" style="left:727px;width:150px">
    <svg width="58" viewBox="0 0 58 60" fill="none" stroke="#fff" stroke-width="1.8"><path d="M29 8l3 6 6 1-4 4 1 6-6-3-6 3 1-6-4-4 6-1z"/><path d="M13 16l2 3 3 .5-2 2 .5 3-3.5-1.5-3 1.5.5-3-2-2 3-.5zM45 16l2 3 3 .5-2 2 .5 3-3.5-1.5-3 1.5.5-3-2-2 3-.5z"/><rect x="3" y="38" width="8" height="14"/><path d="M11 40h14c3 0 4 4 0 4h-6l16 0 16-8c3-1 5 2 2 4L38 50H11"/></svg>
    <h3>KUNDENZUFRIE-<br>DENHEIT</h3>
    <p>Bei KOLVENO steht die Zufriedenheit unserer Kunden an erster Stelle. Wir arbeiten eng mit Ihnen zusammen, um Ihre individuellen Anforderungen zu verstehen und zu erfüllen.</p>
  </div>
  <div class="abs divider" style="left:891px"></div>

  <div class="abs strength" style="left:913px;width:145px">
    <svg width="54" viewBox="0 0 54 60" fill="none" stroke="#fff" stroke-width="1.8"><circle cx="32" cy="30" r="18"/><path d="M32 18v12l7 5M28 8h8M32 8v4M47 14l3-3M2 22h10M5 30h8M2 38h10"/></svg>
    <h3>SCHNELLIGKEIT</h3>
    <p>Unsere kurzen Lieferzeiten und erstklassiger Kundensupport gewährleisten, dass Sie stets bestens betreut werden.</p>
  </div>
</section>

<div class="abs quote-mark" style="left:148px;top:2400px">“</div>
<h2 class="abs section-title testi-title">Was unser Kunde sagt</h2>
<div class="abs testi" style="left:149px">
  <p>Quis ipsum suspendisse ultrices gravida. Risus commodo viverra maecenas accumsan lacus vel facilisis. Risus commodo viverra maecenas accumsan lacus vel facilisis.&nbsp; Lorem ipsum dolor sit amet, consectetur adipiscing elit, sed do eiusmod tempor incididunt ut labore et dolore magna aliqua.</p>
  <p class="name">- Lorenz Haberl</p>
</div>
<div class="abs testi" style="left:634px;width:420px">
  <p>Lorem ipsum dolor sit amet, consectetur adipiscing elit, sed do eiusmod tempor incididunt ut labore et dolore magna aliqua. Quis ipsum suspendisse ultrices gravida. Risus commodo viverra maecenas accumsan lacus vel facilisis.</p>
  <p class="name" style="margin-top:35px">- Miriam Ostrander</p>
</div>
<div class="abs quote-mark" style="left:1003px;top:2600px">”</div>
<div class="abs testi-dots"><i></i><i></i><i></i><i></i><i></i></div>

<section class="abs contact">
  <h2 class="abs section-title">Schneller Kontakt</h2>
  <p class="abs sub">Risus commodo viverra maecenas accumsan lacus vel facilisis.</p>
  <div class="abs field" style="left:227px;top:115px;width:173px;height:39px">Name</div>
  <div class="abs field" style="left:412px;top:115px;width:169px;height:39px">Email</div>
  <div class="abs field" style="left:594px;top:115px;width:170px;height:39px">Telefon</div>
  <div class="abs field" style="left:227px;top:165px;width:537px;height:106px">Wie können wir Ihnen helfen?</div>
  <div class="abs btn-send">SENDEN</div>
  <div class="abs contact-visual" role="img" aria-label="Illustration: eine Person schickt einen großen roten Briefumschlag als Papierflieger los"></div>
</section>

<section class="abs info">
  <div class="abs item addr">
    <svg width="20" height="26" viewBox="0 0 20 26"><path d="M10 0a10 10 0 0 0-10 10c0 7 10 16 10 16s10-9 10-16A10 10 0 0 0 10 0z" fill="#b30b0b"/><circle cx="10" cy="10" r="3.5" fill="#fff"/></svg>
    <span style="margin-left:4px">XXXXXXXXXXXXXXXXXXXXXXXX<br>XXXXXXXXXXXXXXXXXXXXXXXX<br>XXXXXXXXXXXXXXXXXXX</span>
  </div>
  <div class="abs item mail">
    <svg width="22" height="16" viewBox="0 0 22 16" fill="none" stroke="#b30b0b" stroke-width="1.6"><rect x="1" y="1" width="20" height="14"/><path d="M1 1l10 8 10-8"/></svg>
    kontakt@kolveno.de
  </div>
  <div class="abs item tel">
    <svg width="22" height="22" viewBox="0 0 24 24" fill="none" stroke="#b30b0b" stroke-width="1.8"><path d="M22 16.9v3a2 2 0 0 1-2.2 2 19.8 19.8 0 0 1-8.6-3.1 19.5 19.5 0 0 1-6-6A19.8 19.8 0 0 1 2.1 4.2 2 2 0 0 1 4.1 2h3a2 2 0 0 1 2 1.7c.1.9.4 1.8.7 2.7a2 2 0 0 1-.5 2.1L8 9.8a16 16 0 0 0 6 6l1.3-1.3a2 2 0 0 1 2.1-.4c.9.3 1.8.6 2.7.7a2 2 0 0 1 1.7 2z"/></svg>
    0800.472.915
  </div>
</section>

<footer class="abs footer">
  <div class="abs logo"><span class="dot"></span>KOLVENO GmbH</div>
  <div class="abs social"><i></i><i></i><i></i><i></i><i></i></div>
  <div class="abs copy">© 2023 kolveno.de</div>
</footer>

</body>
</html>
```